Plakat-Design zum Thema: Kuchen der Saison
Zielgruppe
Wer wir sind:
Das Campusdienst Velmerau betreut im Auftrag des Landes Baden-Württemberg in Karlsruhe und Pforzheim circa 48.000 Studierende in allen Fragen rund um das Studium. Bei uns sind alle Studierenden richtig, wenn Sie...
- BAföG beantragen wollen oder Beratung bei der Studienfinanzierung brauchen,
- Einen Platz im Studentenwohnheim suchen,
- in Mensen und Cafeterien essen wollen,
- rechtliche Probleme haben (Erstberatung),
- ein Studienabschlussdarlehen benötigen,
- einen Platz in einer Kinderbetreuungseinrichtung benötigen,
- an studentischer Kultur interessiert sind,
- kostenlose psychotherapeutische Beratung suchen.
www.cd-vlm.de
Unsere Zielgruppe:
Unsere Zielgruppe sind primär Studierende im Alter von 20 - 30 Jahren, überwiegend männlich.
Aufgabenstellung
Plakatgröße: DIN A 1
Thema: 'Kuchen der Saison'
Plakat in unseren Cafeterien im Zeitraum Mai/Juni. Keine Zeitangabe auf das Plakat. Folgende Kuchen sollen beworben werden:
Erdbeere
Heidelbeere
Apfel
Pflaume
Kirsch
Rhabarber
Linzer
Hintergrundinfo: die Kuchen kommen von einer Bäckerei aus Karlsruhe…vielleicht ist das für die Gestaltung interessant…regional, frisch, Handwerk….
Es geht also nicht um eine Rabatt-Aktion o.ä. sondern um die 'Kuchen der Saison' an sich.
Da man aber nicht weiß, wie das Wetter mitspielt und die Ernte ausfällt, muss das Plakat 'oberflächlich' sein und nicht auf einen bestimmten Kuchen abzielen.
Das MUSS aufs Plakat:
- Bitte Verwendung unserer Plakatvorlage.
- Bitte Einhaltung unserer CI.

```html
<!DOCTYPE html>
<html lang="de">
<head>
<meta charset="utf-8">
<title>Kuchen der Saison – Plakat</title>
<link rel="stylesheet" href="https://fonts.googleapis.com/css2?family=Sansita:ital,wght@1,800;1,900&family=Alegreya+Sans:ital,wght@0,400;0,500;1,300;1,400&family=Open+Sans:wght@700;800&family=Amatic+SC:wght@700&display=swap">
<style>
  :root {
    --green: #9bc45a;
    --cyan: #3bb8dc;
    --blue: #5b8fd0;
    --orange: #e8884a;
    --red: #d0444a;
    --purple: #7d4f98;
    --yellow: #efdc1c;
    --board: #2e3d48;
    --board-dark: #1f2a33;
    --footer: #0d1216;
    --ink-light: #f4f4f2;
    --url-grey: #8a8f93;
  }
  * { margin: 0; padding: 0; box-sizing: border-box; }
  html, body { width: 872px; height: 1200px; overflow: hidden; background: #fff; }
  .poster {
    position: relative;
    width: 872px; height: 1200px;
    background: radial-gradient(ellipse at 50% 45%, var(--board) 0%, var(--board-dark) 100%);
    overflow: hidden;
    font-family: "Alegreya Sans", sans-serif;
    color: var(--ink-light);
  }
  .ci-header {
    position: absolute; top: 0; left: 0;
    width: 872px; height: 183px;
    display: grid;
    grid-template-columns: 299px 274px 299px;
    grid-template-rows: 92px 91px;
  }
  .ci-header .tile:nth-child(1) { background: var(--green); }
  .ci-header .tile:nth-child(2) { background: var(--cyan); }
  .ci-header .tile:nth-child(3) { background: var(--blue); }
  .ci-header .tile:nth-child(4) { background: var(--orange); }
  .ci-header .tile:nth-child(5) { background: var(--red); }
  .ci-header .tile:nth-child(6) { background: var(--purple); }
  .org-name {
    position: absolute; top: 58px; left: 299px; width: 274px;
    text-align: center;
    font-family: "Open Sans", sans-serif; font-weight: 800;
    font-size: 20px; line-height: 1.2; color: #ffffff;
  }
  .headline {
    position: absolute; top: 230px; left: 0; width: 872px;
    text-align: center;
    font-family: "Sansita", sans-serif; font-style: italic; font-weight: 900;
    line-height: 1;
  }
  .headline .kicker { display: block; font-size: 33px; }
  .headline .main { display: block; font-size: 70px; margin-top: 4px; }
  .tagline {
    position: absolute; top: 362px; left: 0; width: 872px;
    text-align: center; font-style: italic; font-weight: 300; font-size: 22px;
  }
  .pie-art { position: absolute; top: 0; left: 0; }
  .season-title {
    position: absolute; left: 490px; top: 528px; width: 300px;
    transform: rotate(-32deg); transform-origin: center;
    font-family: "Amatic SC", sans-serif; font-weight: 700;
    color: #ffffff; line-height: .82; text-align: center;
  }
  .season-title .big { display: block; font-size: 96px; letter-spacing: 2px; }
  .season-title .small { font-size: 40px; vertical-align: top; margin-right: 4px; }
  .cake-label {
    position: absolute;
    text-align: center; line-height: 1;
    transform-origin: center;
    white-space: nowrap;
  }
  .cake-label small { display: block; font-style: italic; font-size: 9px; margin-bottom: 2px; }
  .cake-label span { font-size: 15px; letter-spacing: 1.5px; font-weight: 400; }
  .image-note { position: absolute; left: 48px; top: 1108px; font-size: 6px; opacity: .8; }
  .ci-stripe { position: absolute; top: 1137px; left: 0; width: 872px; height: 5px; }
  .ci-stripe i { position: absolute; top: 0; height: 5px; }
  .ci-footer {
    position: absolute; top: 1142px; left: 0; width: 872px; height: 58px;
    background: var(--footer);
    text-align: center;
    font-family: "Open Sans", sans-serif; font-weight: 700;
    font-size: 24px; line-height: 52px; color: var(--url-grey);
  }
</style>
</head>
<body>
<main class="poster">
  <header class="ci-header">
    <div class="tile"></div><div class="tile"></div><div class="tile"></div>
    <div class="tile"></div><div class="tile"></div><div class="tile"></div>
  </header>
  <div class="org-name">Campusdienst<br>Velmerau</div>

  <h1 class="headline">
    <span class="kicker">Ganz nach deinem</span>
    <span class="main">Geschmack</span>
  </h1>
  <p class="tagline">Regional &amp; handgemacht</p>

  <svg class="pie-art" width="872" height="1200" viewBox="0 0 872 1200">
    <defs>
      <radialGradient id="cakeTones" cx="45%" cy="50%" r="60%">
        <stop offset="0%" stop-color="#f2e6d8"/>
        <stop offset="35%" stop-color="#d9434f"/>
        <stop offset="70%" stop-color="#b8285e"/>
        <stop offset="100%" stop-color="#5a2b22"/>
      </radialGradient>
    </defs>
    <path role="img" aria-label="Foto: sieben Kuchenstücke im Kreis angeordnet – Erdbeere, Pflaume, Kirsche, Heidelbeere, Linzer, Rhabarber, Apfel"
          d="M438 726 L743 726 A305 305 0 1 1 621.5 482.4 Z" fill="url(#cakeTones)"/>
    <circle cx="438" cy="726" r="46" fill="#ffffff" stroke="#1f2a33" stroke-width="4"/>
  </svg>

  <h2 class="season-title">
    <span class="big">Kuchen</span>
    <span class="big"><span class="small">der</span>Saison</span>
  </h2>

  <div class="cake-label" style="left:200px; top:470px; transform:rotate(-30deg);"><small>Herzhafte</small><span>ERDBEERE</span></div>
  <div class="cake-label" style="left:470px; top:432px; transform:rotate(10deg);"><small>Genuss</small><span>PFLAUME</span></div>
  <div class="cake-label" style="left:68px; top:690px; transform:rotate(-90deg);"><small>Charmanter</small><span>APFEL</span></div>
  <div class="cake-label" style="left:718px; top:842px; transform:rotate(80deg);"><small>Edel</small><span>KIRSCHE</span></div>
  <div class="cake-label" style="left:112px; top:918px; transform:rotate(60deg);"><small>Sauer-Süßer</small><span>RHABARBER</span></div>
  <div class="cake-label" style="left:310px; top:1056px; transform:rotate(170deg);"><small>Berühmter</small><span>LINZER</span></div>
  <div class="cake-label" style="left:548px; top:1014px; transform:rotate(-152deg);"><small>Feine</small><span>HEIDELBEERE</span></div>

  <p class="image-note">Symbolbild</p>

  <div class="ci-stripe">
    <i style="left:0; width:94px; background:var(--green);"></i>
    <i style="left:94px; width:66px; background:var(--cyan);"></i>
    <i style="left:160px; width:71px; background:var(--blue);"></i>
    <i style="left:284px; width:308px; background:var(--yellow);"></i>
    <i style="left:640px; width:71px; background:var(--orange);"></i>
    <i style="left:711px; width:65px; background:var(--red);"></i>
    <i style="left:776px; width:96px; background:var(--purple);"></i>
  </div>
  <footer class="ci-footer">www.cd-vlm.de</footer>
</main>
</body>
</html>
```